Plofzon car advertisement

de website moet uit minimaal 3 pagina's bestaan. 1 pagina als een landingspagina. 1 pagina voor consumenten die hun auto willen laten beplakken met bedrijfsreclame en 1 pagina voor bedrijven / consumenten die hun bedrijfsreclame op een consumentenauto wilt plaatsen.

de website moet echt een happy website zijn. consumenten kunnen geld verdienen met reclame op hun auto te laten zetten en bedrijven kunnen voor een relatief goedkoop bedrag hun bedrijfsreclame op een auto laten zetten. die auto rijdt dan rond en veel mensen zien de reclame.

beide pagina's moeten dus een glimlach opleveren.

het doel van de startpagina is dat je door kunt gaan naar de consumenten en de bedrijfspagina.

gebruik leuke, vrolijke kleuren en vormen en zorg dat de mensen een glimlach krijgen als ze naar de website kijken.

doelgroep is consumenten die een auto rijden en geld willen verdienen met hun auto en de zakelijke ondernemer die voor een goedkoop bedrag zijn bedrijfsreclame met een full carwrap kan laten zien aan de buitenwereld.

doordat consumenten zich bij ons aanmelden hebben wij een database met auto's en weten we hoeveel deze auto's rijden en in welke regio's ze rijden en wat voor auto ze rijden. allemaal hele belangrijke informatie voor een ondernemer die reclame wilt maken op ene specifieke auto type en in een bepaalde regio.

-

website should consist of at least 3 pages. 1 landing page, 1 customer page and 1 business page. landing page let's the visitor choose wether he / she is a customer with a car and wants to allow his car to be fully carwrapped or he / she is a business owner who wants to place his advertisement on a car.

website should be a really happy joyfull website and bring a smile to the visitor. beause the customer can earn money (200 euro / month nett) by allowing advertisements on his car (full car wrap) and the business owner because for a low price he can advertise.

when customers that owns a car register themselves with our website we build a database with cars in specific locations. a business owner wants to advertise his product into a specific region. this is very valuable information.

agreement is 1 year for a customer to have advertisements on his car and for a business to advertise. after that year, the advertisements are safely removed from the car and new advertisement agreements can be made. a business can place advertisements (full carwrap) already for 795 euro's., Details for my new Web Design Project will be added soon. , de website moet uit minimaal 3 pagina's bestaan. 1 pagina als een landingspagina. 1 pagina voor consumenten die hun auto willen laten beplakken met bedrijfsreclame en 1 pagina voor bedrijven / consumenten die hun bedrijfsreclame op een consumentenauto wilt plaatsen.

Target Market(s)

customers who has a car
businesses who want to advertise their business / product on a car

Industry/Entity Type

Business

Requirements
Must have
• website should be playfull, colorfull and a joy to look at and work with. altough functoinality is very limited visitors need to be intrigued to proceed to contact plofzon.
Nice to have
• nice graphics, moving images, a "living" website (not so static)

```html
<!DOCTYPE html>
<html lang="en">
<head>
<meta charset="utf-8">
<title>Plofzon Car</title>
<link rel="stylesheet" href="https://fonts.googleapis.com/css2?family=Anton&family=Ubuntu:wght@400;500;700&family=Arimo:wght@400;700&display=swap">
<style>
  :root {
    --blue: #1f74cf;
    --blue-deep: #1a5aa8;
    --blue-light: #4aa0e6;
    --sun: #ffb400;
    --sun-dark: #e48a00;
    --leaf: #52c234;
    --leaf-dark: #319a1c;
    --text: #444;
    --footer-bg: #eef3f8;
    --border: #c9c9c9;
    --white: #fff;
  }
  * { box-sizing: border-box; margin: 0; padding: 0; }
  html, body { width: 920px; height: 1200px; overflow: hidden; background: var(--white); }
  body { position: relative; font-family: "Arimo", Arial, sans-serif; color: var(--text); }

  .brand { position: absolute; left: 28px; top: 60px; display: flex; align-items: center; gap: 10px; }
  .brand-mark { width: 26px; height: 26px; border-radius: 50%; background: var(--sun); }
  .brand-name { font-family: "Anton", sans-serif; font-size: 30px; color: var(--blue); letter-spacing: .5px; line-height: 1; }

  .top-icons { position: absolute; left: 698px; top: 51px; display: flex; gap: 24px; }
  .top-icon { width: 39px; height: 29px; display: flex; align-items: center; justify-content: center; border-radius: 6px; }
  .top-icon.is-active { background: linear-gradient(#4aa0e6, #1f74cf); }

  .main-nav { position: absolute; left: 28px; top: 104px; width: 864px; height: 46px; display: flex;
    background: linear-gradient(#58aaeb, #2a82d8 50%, #1f74cf 51%, #2b86dc); border-radius: 8px 8px 0 0; border-bottom: 1px solid #aed0f2; }
  .main-nav a { color: var(--white); text-decoration: none; font-family: "Ubuntu", sans-serif; font-size: 14px; display: flex; align-items: center; justify-content: center; border-right: 1px solid #1b62b5; position: relative; }
  .main-nav a:last-child { border-right: none; }
  .main-nav a.is-current::after { content: ""; position: absolute; bottom: 0; left: 50%; margin-left: -4px; border: 4px solid transparent; border-bottom-color: #fff; }

  .hero { position: absolute; left: 28px; top: 150px; width: 864px; height: 255px; overflow: hidden; background: linear-gradient(100deg, #7c9ec4 0%, #3d76b9 45%, #2a6bbd 100%); }
  .hero-sun { position: absolute; left: 330px; top: -60px; width: 150px; height: 150px; border-radius: 50%; background: radial-gradient(circle, rgba(255,210,80,.55), rgba(255,210,80,0) 70%); }
  .hero-car { position: absolute; right: 30px; top: 40px; width: 440px; height: 200px; border-radius: 70px 110px 30px 30px; background: radial-gradient(ellipse at 50% 40%, #f2f4f6, #c7ccd2 70%, #9aa3ad); }
  .hero-title { position: absolute; left: 34px; top: 88px; font-family: "Anton", sans-serif; font-weight: 400; font-size: 32px; line-height: 40px; color: var(--white); text-shadow: 0 2px 3px rgba(0,0,0,.35); }
  .hero-choices { position: absolute; left: 34px; top: 150px; display: flex; gap: 12px; }
  .choice { display: block; width: 172px; padding: 9px 14px; border-radius: 22px; color: var(--white); text-decoration: none; font-family: "Ubuntu", sans-serif; font-size: 14px; font-weight: 700; line-height: 17px; box-shadow: 0 3px 0 rgba(0,0,0,.2); }
  .choice small { display: block; font-weight: 400; font-size: 11px; }
  .choice.for-drivers { background: linear-gradient(#ffc93a, var(--sun-dark)); }
  .choice.for-business { background: linear-gradient(#74d957, var(--leaf-dark)); }
  .hero-reflection { position: absolute; left: 28px; top: 405px; width: 864px; height: 30px; background: linear-gradient(#e4e8ec, #fff); }

  .gallery { position: absolute; left: 28px; top: 453px; width: 864px; display: flex; justify-content: space-between; }
  .gallery-item { width: 271px; height: 139px; border: 3px solid #fff; border-radius: 6px; box-shadow: 0 0 0 1px var(--border), 0 2px 4px rgba(0,0,0,.2); }
  .gallery-item.wrap-work { background: linear-gradient(120deg, #8a8f96, #d8dde3 50%, #4f7ac6); }
  .gallery-item.door { background: linear-gradient(100deg, #5d6774, #bfc5cc 55%, #7d6555); }
  .gallery-item.bonnet { background: linear-gradient(#8fa3c0, #b9c0c8 60%, #6f7680); }

  .content { position: absolute; left: 30px; top: 620px; width: 562px; font-size: 11px; line-height: 20px; }
  .welcome { font-family: "Anton", sans-serif; font-weight: 400; font-size: 24px; color: var(--blue); line-height: 34px; margin-bottom: 22px; }
  .content p { margin-bottom: 10px; }
  .feature { display: flex; gap: 20px; margin-bottom: 16px; }
  .feature-photo { flex: none; width: 220px; height: 142px; border: 1px solid var(--border); border-radius: 6px; padding: 5px; }
  .feature-photo div { width: 100%; height: 100%; border-radius: 3px; background: linear-gradient(110deg, #5b6f58, #c9ced6 45%, #6e8ad0 75%, #d5843c); }
  .feature p { margin: 0; }
  .content strong { color: var(--blue-deep); }

  .sidebar { position: absolute; left: 612px; top: 608px; width: 280px; height: 434px; border-radius: 8px; background: linear-gradient(#2c85da, #1f74cf 60%, #1a66c0); color: var(--white); overflow: hidden; }
  .side-head { height: 52px; padding-left: 45px; font-family: "Ubuntu", sans-serif; font-weight: 400; font-size: 23px; line-height: 56px; color: #e9f3ff; background: linear-gradient(#4aa0e6, #2b86dc); }
  .news { padding: 22px 20px 0 45px; height: 171px; font-family: "Ubuntu", sans-serif; font-size: 11px; line-height: 20px; }
  .news li { list-style: none; position: relative; margin-bottom: 12px; }
  .news li::before, .links li::before { content: "\2192"; position: absolute; left: -17px; font-size: 9px; color: #bcdaf7; }
  .news time { font-weight: 500; display: block; }
  .login { padding: 20px 20px 0 45px; font-family: "Ubuntu", sans-serif; font-size: 11.5px; }
  .field { display: flex; align-items: center; margin-bottom: 7px; }
  .field label { width: 84px; font-weight: 500; }
  .field input { width: 115px; height: 15px; border: 1px solid #9cc5ee; }
  .remember { display: flex; align-items: center; margin: 10px 0 14px; }
  .remember input { width: 13px; height: 13px; margin: 0 30px 0 8px; }
  .remember button { width: 70px; height: 22px; border: 1px solid #ffe08a; border-radius: 11px; background: linear-gradient(#ffc93a, var(--sun-dark)); color: #fff; font-family: "Ubuntu", sans-serif; font-size: 12px; font-weight: 500; }
  .links li { list-style: none; position: relative; line-height: 22px; }
  .links a { color: #fff; }

  .site-footer-nav { position: absolute; left: 28px; top: 1090px; width: 864px; height: 42px; background: var(--footer-bg); border-radius: 6px; font-size: 11.5px; font-weight: 700; }
  .site-footer-nav a, .site-footer-nav span { position: absolute; top: 14px; }
  .site-footer-nav a { color: var(--blue-deep); }
  .site-footer-nav span { color: #8aa; font-weight: 400; }
  .copyright { position: absolute; left: 34px; top: 1164px; font-size: 11.5px; color: #333; }
</style>
</head>
<body>
  <header>
    <div class="brand"><span class="brand-mark"></span><span class="brand-name">PLOFZON CAR</span></div>
    <div class="top-icons">
      <span class="top-icon is-active"><svg width="13" height="12" viewBox="0 0 13 12"><path d="M1 6 6.5 1 12 6M3 5v6h7V5" fill="none" stroke="#fff" stroke-width="1.2"/></svg></span>
      <span class="top-icon"><svg width="13" height="10" viewBox="0 0 13 10"><rect x=".5" y=".5" width="12" height="9" fill="none" stroke="#333"/><path d="M.5.5 6.5 6 12.5.5" fill="none" stroke="#333"/></svg></span>
      <span class="top-icon"><svg width="13" height="11" viewBox="0 0 13 11"><rect x="1" y="1" width="11" height="3" fill="none" stroke="#333"/><path d="M6.5 4v3M2.5 7h8M2.5 7v3M10.5 7v3M6.5 7v3" stroke="#333"/></svg></span>
    </div>
  </header>

  <nav class="main-nav">
    <a href="#" class="is-current" style="width:155px">HOME</a>
    <a href="#" style="width:163px">FOR DRIVERS</a>
    <a href="#" style="width:180px">FOR BUSINESS</a>
    <a href="#" style="width:186px">CONTACTS</a>
    <a href="#" style="width:180px">SITE MAP</a>
  </nav>

  <section class="hero">
    <div class="hero-sun"></div>
    <div class="hero-car" role="img" aria-label="Bright white compact SUV wearing a cheerful full car wrap"></div>
    <h1 class="hero-title">Wrap your car, win a smile!</h1>
    <div class="hero-choices">
      <a href="#" class="choice for-drivers">I drive a car<small>Earn €200 net a month</small></a>
      <a href="#" class="choice for-business">I own a business<small>Full wrap from €795</small></a>
    </div>
  </section>
  <div class="hero-reflection"></div>

  <div class="gallery">
    <div class="gallery-item wrap-work" role="img" aria-label="Installer applying wrap film to the side of a car"></div>
    <div class="gallery-item door" role="img" aria-label="Hands smoothing wrap film onto a car door"></div>
    <div class="gallery-item bonnet" role="img" aria-label="Front of a wrapped silver hatchback"></div>
  </div>

  <main class="content">
    <h2 class="welcome">Welcome to PLOFZON CAR</h2>
    <p>Plofzon brings drivers and businesses together. Drivers get paid to show a colourful full car wrap, and businesses get their message seen all over town for a small price. Pick your side above and let's get rolling!</p>
    <div class="feature">
      <div class="feature-photo"><div role="img" aria-label="Hatchback covered in a full advertising wrap parked outdoors"></div></div>
      <p><strong>Drive a car?</strong> Sign up, tell us what you drive and where, and we match you with a business. We wrap your car for free and you earn €200 net every month. After one year the wrap is removed safely and you can start a new deal.<br><strong>Own a business?</strong> Choose a car type and a region from our growing list of drivers. For just €795 your brand rides around for a whole year, seen by thousands every day.</p>
    </div>
    <p>Every driver who joins adds to our map of cars, regions and kilometres driven. That means your advert goes exactly where your customers are. Happy drivers, happy businesses, and a few extra smiles on the road!</p>
  </main>

  <aside class="sidebar">
    <h3 class="side-head">Latest News</h3>
    <ul class="news">
      <li><time>May 21, 2010</time>Drivers now earn €200 net a month with a full Plofzon wrap.</li>
      <li><time>May 12, 2010</time>Businesses can advertise on a car for a year from €795.</li>
    </ul>
    <h3 class="side-head">Login Form</h3>
    <form class="login">
      <div class="field"><label>Username:</label><input type="text"></div>
      <div class="field"><label>Password:</label><input type="password"></div>
      <div class="remember">Remember Me:<input type="checkbox"><button type="button">Log In</button></div>
      <ul class="links">
        <li><a href="#">Forgot your password?</a></li>
        <li><a href="#">Register</a></li>
      </ul>
    </form>
  </aside>

  <footer>
    <nav class="site-footer-nav">
      <a href="#" style="left:6px">Home</a><span style="left:101px">|</span>
      <a href="#" style="left:166px">Drivers</a><span style="left:261px">|</span>
      <a href="#" style="left:326px">Business</a><span style="left:431px">|</span>
      <a href="#" style="left:496px">Contacts</a><span style="left:608px">|</span>
      <a href="#" style="left:672px">Sitemap</a>
    </nav>
    <p class="copyright">Copyright text here</p>
  </footer>
</body>
</html>
```